business card letterhead envelope
Darren Holcomb Realtors
Project: business card letterhead envelope
business card letterhead envelope - Real Estate
Creative Brief
Professional
Darren Holcomb
Attorney/Broker
2817 W. Larkspur Ave Suite B7 Odessa, TX 79748
Darren@PecosPrairieHouses.com
PecosPrairieHouses.com

```html
<!DOCTYPE html>
<html lang="en">
<head>
<meta charset="utf-8">
<title>Darren Holcomb Realtors – Stationery</title>
<link rel="stylesheet" href="https://fonts.googleapis.com/css2?family=Cinzel:wght@400&family=Open+Sans:wght@400;600&display=swap">
<style>
:root{
  --backdrop:#e7e4df;
  --paper:#ffffff;
  --paper-shade:#f1f1f1;
  --ink:#1c1c1c;
  --ink-soft:#555555;
  --card-dark-1:#2e2e2e;
  --card-dark-2:#0b0b0b;
  --on-dark:#ffffff;
  --on-dark-soft:#bdbdbd;
  --shadow:0 3px 10px rgba(0,0,0,.18);
}
*{box-sizing:border-box;margin:0;padding:0}
html,body{width:1200px;height:763px;overflow:hidden}
body{background:var(--backdrop);font-family:"Open Sans",Arial,sans-serif;color:var(--ink);position:relative}
.sheet{position:absolute;box-shadow:var(--shadow)}

/* brand lockup */
.brand{display:flex;flex-direction:column;align-items:center;gap:6px}
.brand-dot{border-radius:50%;background:var(--ink)}
.brand-name{font-family:"Cinzel",Georgia,serif;font-weight:400;text-transform:uppercase;letter-spacing:.08em;text-align:center;line-height:1.25;color:var(--ink)}
.on-dark .brand-dot{background:var(--on-dark)}
.on-dark .brand-name{color:var(--on-dark)}

/* letterhead */
.letterhead{left:300px;top:70px;width:470px;height:608px;background:var(--paper)}
.letterhead .brand{position:absolute;left:36px;top:34px}
.letterhead .brand-dot{width:34px;height:34px}
.letterhead .brand-name{font-size:11px;width:140px}
.letterhead .sender{position:absolute;right:34px;top:40px;font-size:6.5px;line-height:1.55;color:var(--ink-soft);text-align:right}
.web-band{position:absolute;left:0;right:0;bottom:0;height:22px;background:var(--ink);color:var(--on-dark);font-size:8px;font-weight:600;letter-spacing:.05em;display:flex;align-items:center;justify-content:center}

/* envelopes */
.envelope{width:370px;height:165px;background:var(--paper)}
.envelope-back{left:800px;top:70px}
.envelope-back svg{position:absolute;inset:0}
.envelope-back .brand{position:absolute;left:50%;top:16px;transform:translateX(-50%)}
.envelope-back .brand-dot{width:22px;height:22px}
.envelope-back .brand-name{font-size:7px;width:130px}
.envelope-front{left:800px;top:255px}
.envelope-front .brand{position:absolute;left:22px;top:16px}
.envelope-front .brand-dot{width:22px;height:22px}
.envelope-front .brand-name{font-size:7px;width:110px}
.envelope-front .return{position:absolute;left:22px;top:72px;font-size:5.5px;color:var(--ink-soft)}
.envelope-front .web-band{height:12px;font-size:6px}

/* business cards */
.card{width:250px;height:143px;border-radius:8px;overflow:hidden}
.card-dark{background:linear-gradient(180deg,var(--card-dark-1),var(--card-dark-2))}
.card-light{background:linear-gradient(180deg,var(--paper),var(--paper-shade))}
.card-front .brand{position:absolute;left:18px;top:26px}
.card-front .brand-dot{width:30px;height:30px}
.card-front .brand-name{font-size:9px;width:110px}
.card-front .contact{position:absolute;left:138px;top:28px;font-size:5.8px;line-height:1.55;color:var(--ink-soft)}
.card-front .contact strong{display:block;font-size:7px;font-weight:600;color:var(--ink)}
.card-dark .contact{color:var(--on-dark-soft)}
.card-dark .contact strong{color:var(--on-dark)}
.card-back .brand{position:absolute;left:50%;top:24px;transform:translateX(-50%)}
.card-back .brand-dot{width:52px;height:52px}
.card-back .brand-name{font-size:9px;width:170px}
.card .url{position:absolute;left:0;right:0;bottom:10px;text-align:center;font-size:6px;letter-spacing:.06em;color:var(--ink-soft)}
.card-dark .url{color:var(--on-dark-soft)}

.dark-front{left:25px;top:200px}
.dark-back{left:25px;top:370px}
.light-front{left:860px;top:440px}
.light-back{left:860px;top:600px}
</style>
</head>
<body>

<section class="sheet letterhead">
  <div class="brand"><span class="brand-dot"></span><span class="brand-name">Darren Holcomb Realtors</span></div>
  <address class="sender">
    2817 W. Larkspur Ave Suite B7<br>Odessa, TX 79748<br>Phone 432.555.0148<br>Fax 432.555.0162<br>Email: Darren@PecosPrairieHouses.com
  </address>
  <div class="web-band">www.PecosPrairieHouses.com</div>
</section>

<section class="sheet envelope envelope-back">
  <svg width="370" height="165" viewBox="0 0 370 165">
    <polyline points="0,165 185,85 370,165" fill="none" stroke="#d6d6d6" stroke-width="1"/>
    <polygon points="0,0 370,0 185,78" fill="#1c1c1c"/>
  </svg>
  <div class="brand on-dark"><span class="brand-dot"></span></div>
</section>

<section class="sheet envelope envelope-front">
  <div class="brand"><span class="brand-dot"></span><span class="brand-name">Darren Holcomb Realtors</span></div>
  <address class="return">2817 W. Larkspur Ave Suite B7 Odessa, TX 79748</address>
  <div class="web-band">www.PecosPrairieHouses.com</div>
</section>

<section class="sheet card card-dark card-front dark-front on-dark">
  <div class="brand"><span class="brand-dot"></span><span class="brand-name">Darren Holcomb Realtors</span></div>
  <address class="contact">
    <strong>Darren Holcomb</strong>Attorney/Broker<br><br>2817 W. Larkspur Ave Suite B7<br>Odessa, TX 79748<br>Phone 432.555.0148<br>Cell 432.555.0173<br>Darren@PecosPrairieHouses.com
  </address>
</section>

<section class="sheet card card-dark card-back dark-back on-dark">
  <div class="brand"><span class="brand-dot"></span><span class="brand-name">Darren Holcomb Realtors</span></div>
  <div class="url">www.PecosPrairieHouses.com</div>
</section>

<section class="sheet card card-light card-front light-front">
  <div class="brand"><span class="brand-dot"></span><span class="brand-name">Darren Holcomb Realtors</span></div>
  <address class="contact">
    <strong>Darren Holcomb</strong>Attorney/Broker<br><br>2817 W. Larkspur Ave Suite B7<br>Odessa, TX 79748<br>Phone 432.555.0148<br>Cell 432.555.0173<br>Darren@PecosPrairieHouses.com
  </address>
  <div class="url">www.PecosPrairieHouses.com</div>
</section>

<section class="sheet card card-light card-back light-back">
  <div class="brand"><span class="brand-dot"></span><span class="brand-name">Darren Holcomb Realtors</span></div>
  <div class="url">www.PecosPrairieHouses.com</div>
</section>

</body>
</html>
```